Business Card Design for Kidlarko (Hires out childrens play areas)

Looking to have a business card designed for a company we just bought. The company rents out childrens play areas.

I have uploaded a couple of examples of the kind of business card style I like. Here are two more examples:

https://vesterlingstudio.example.nz/project/brisk-romp-branding/
https://imgvaultcdn.example.com/design_img/8462913/307481/307481_2958174_8462913_a7c3e190_image.jpg

I think a white card will be best due to all the colours in the logo.

Size we require: 3.75" x 2.25" (horizontally orientated) with a 0.125" bleed

Uploaded is two versions of our logo.

Details for the card:
1. My name: Wade Ferrin
2. Title: Managing Director
3. Phone no: 021 537 462
4. Email: wade@kidlarko.example.nz
5. URL: www.kidlarko.example.nz
6. Address:
PO Box 381627
Fernmoor, Auckland

Let me know if you need anything else.

Target Market(s)

Hospitals, doctors surgeries, bed shops, etc.

Contact Information for Business Card

Details for the card:
1. My name: Wade Ferrin
3. Phone no: 021 537 462
5. URL: www.kidlarko.example.nz
6. Address:
PO Box 381627
Fernmoor, Auckland

Requirements
Should not have
• Not too busy.

```html
<!DOCTYPE html>
<html lang="en">
<head>
<meta charset="utf-8">
<title>Kidlarko — Business Card</title>
<link href="https://fonts.googleapis.com/css2?family=Nunito+Sans:wght@400;600;800&display=swap" rel="stylesheet">
<style>
  :root{
    --backdrop:#cfe0e8;
    --card:#ffffff;
    --peach:#fbdcbf;
    --peach-soft:#fdeadb;
    --orange:#f3961f;
    --navy:#24468a;
    --slate:#5c6f9c;
    --teal:#1fa3a6;
    --red:#e2262f;
    --green:#3aa845;
    --icon:#f2a868;
  }
  *{box-sizing:border-box;margin:0;padding:0}
  html,body{width:1200px;height:1198px;overflow:hidden}
  body{background:var(--backdrop);position:relative;font-family:"Nunito Sans",Arial,sans-serif}
  .card{position:absolute;width:648px;height:390px;background:var(--card);overflow:hidden;box-shadow:0 10px 22px rgba(40,60,80,.18)}
  .card--front{left:276px;top:152px}
  .card--back{left:278px;top:658px}

  .front-art{position:absolute;left:0;top:0}
  .brand{position:absolute;display:flex;align-items:center;gap:10px;font-weight:800;color:var(--navy);letter-spacing:.5px}
  .brand__dot{border-radius:50%;background:var(--orange)}
  .card--front .brand{left:48px;top:172px;font-size:44px}
  .card--front .brand__dot{width:26px;height:26px}

  .person__name{position:absolute;left:364px;top:46px;font-size:44px;font-weight:400;color:var(--orange);line-height:1}
  .person__title{position:absolute;left:365px;top:104px;font-size:19px;color:var(--slate)}

  .contact{position:absolute;left:368px;top:190px;list-style:none}
  .contact__item{display:flex;align-items:center;height:32.5px;font-size:18px;color:var(--navy)}
  .contact__icon{width:20px;height:20px;margin-right:16px;flex:none}
  .contact__item--cont{padding-left:36px}

  .edge-bar{position:absolute;right:0;width:9px}
  .bottom-bar{position:absolute;bottom:0;height:9px;width:80px}

  .back-pattern{position:absolute;inset:0;background:var(--peach-soft)}
  .card--back .brand{left:50%;top:50%;transform:translate(-50%,-50%);font-size:58px}
  .card--back .brand__dot{width:34px;height:34px}
</style>
</head>
<body>

<section class="card card--front">
  <svg class="front-art" width="340" height="390" viewBox="0 0 340 390" role="img" aria-label="Large soft peach character illustration">
    <path d="M0 0H300C330 90 340 250 270 390H0Z" fill="var(--peach)"/>
  </svg>
  <div class="brand"><span class="brand__dot"></span>Kidlarko</div>

  <h1 class="person__name">Wade Ferrin</h1>
  <p class="person__title">Managing Director</p>

  <ul class="contact">
    <li class="contact__item">
      <svg class="contact__icon" viewBox="0 0 20 20" fill="none" stroke="var(--icon)" stroke-width="1.4"><path d="M4 2l3 1 1 4-2 1c1 3 3 5 6 6l1-2 4 1 1 3-2 2C9 18 2 11 2 4z"/></svg>
      021 537 462</li>
    <li class="contact__item">
      <svg class="contact__icon" viewBox="0 0 20 20" fill="none" stroke="var(--icon)" stroke-width="1.4"><rect x="2" y="4" width="16" height="12"/><path d="M2 4l8 7 8-7"/></svg>
      wade@kidlarko.example.nz</li>
    <li class="contact__item">
      <svg class="contact__icon" viewBox="0 0 20 20" fill="none" stroke="var(--icon)" stroke-width="1.4"><circle cx="10" cy="10" r="8"/><circle cx="10" cy="10" r="3"/><path d="M10 2v5M10 13v5M2 10h5M13 10h5"/></svg>
      www.kidlarko.example.nz</li>
    <li class="contact__item">
      <svg class="contact__icon" viewBox="0 0 20 20" fill="none" stroke="var(--icon)" stroke-width="1.4"><path d="M10 19s6-7 6-11a6 6 0 0 0-12 0c0 4 6 11 6 11z"/><circle cx="10" cy="8" r="2"/></svg>
      PO Box 381627</li>
    <li class="contact__item contact__item--cont">Fernmoor, Auckland</li>
  </ul>

  <span class="edge-bar" style="top:18px;height:84px;background:var(--teal)"></span>
  <span class="edge-bar" style="top:110px;height:80px;background:var(--red)"></span>
  <span class="edge-bar" style="top:200px;height:80px;background:var(--green)"></span>
  <span class="edge-bar" style="top:292px;height:80px;background:var(--orange)"></span>
</section>

<section class="card card--back">
  <div class="back-pattern" role="img" aria-label="Soft peach repeating pattern of smiling character heads"></div>
  <div class="brand"><span class="brand__dot"></span>Kidlarko</div>
  <span class="bottom-bar" style="left:150px;background:var(--orange)"></span>
  <span class="bottom-bar" style="left:242px;background:var(--green)"></span>
  <span class="bottom-bar" style="left:334px;background:var(--red)"></span>
  <span class="bottom-bar" style="left:425px;background:var(--teal)"></span>
</section>

</body>
</html>
```